Presntation folder
Larkvale Home Health Care
The Care you Deserve
we need a design for a presentation folder that would work with our logo design(done in the past by the brand mark foundry)
If you can incorporate this gold seal and text in your design
(Larkvale Home Health has earned the Meridane Council Azure Crest of Merit)

```html
<!DOCTYPE html>
<html lang="en">
<head>
<meta charset="utf-8">
<title>Larkvale Home Health Care — Presentation Folder</title>
<link rel="stylesheet" href="https://fonts.googleapis.com/css2?family=Roboto+Condensed:wght@700&family=Roboto:wght@400&display=swap">
<style>
  :root {
    --backdrop: #d9d9d9;
    --paper: #ffffff;
    --brand-blue: #1d4b8a;
    --brand-navy: #173c72;
    --brand-green: #7cc142;
    --faint-tint: #e4eaf1;
  }
  html, body {
    margin: 0;
    width: 1200px;
    height: 956px;
    overflow: hidden;
    background: var(--backdrop);
  }
  .folder {
    position: absolute;
    left: 111px;
    top: 78px;
    width: 917px;
    height: 816px;
    box-shadow: 0 6px 18px rgba(0,0,0,0.25);
  }
  .folder-art {
    position: absolute;
    inset: 0;
    display: block;
  }
  .wordmark {
    position: absolute;
    font-family: "Roboto Condensed", sans-serif;
    font-weight: 700;
    color: var(--brand-blue);
    margin: 0;
    display: flex;
    align-items: center;
    gap: 8px;
    line-height: 1.05;
  }
  .wordmark-dot {
    width: 22px;
    height: 22px;
    border-radius: 50%;
    background: var(--brand-blue);
    flex: none;
  }
  .wordmark--cover {
    left: 505px;
    top: 30px;
    font-size: 22px;
  }
  .wordmark--back {
    left: 190px;
    top: 508px;
    font-size: 13px;
  }
  .wordmark--back .wordmark-dot { width: 14px; height: 14px; }
  .contact-line {
    position: absolute;
    left: 0;
    width: 456px;
    top: 573px;
    margin: 0;
    text-align: center;
    font-family: "Roboto", sans-serif;
    font-size: 6px;
    color: var(--brand-blue);
  }
</style>
</head>
<body>
<div class="folder">
  <svg class="folder-art" width="917" height="816" viewBox="0 0 917 816" xmlns="http://www.w3.org/2000/svg">
    <rect class="back-panel" x="0" y="0" width="456" height="816" fill="var(--paper)"/>
    <rect class="cover-panel" x="456" y="0" width="461" height="816" fill="var(--paper)"/>
    <rect class="cover-spine-band" x="464" y="0" width="28" height="610" fill="var(--brand-blue)"/>

    <circle class="cover-faint-emblem" cx="748" cy="420" r="100" fill="var(--faint-tint)" role="img" aria-label="Faint brand emblem decoration"/>

    <!-- back pocket -->
    <path class="pocket pocket--back" d="M0 608 H430 L456 640 V816 H0 Z" fill="var(--brand-blue)"/>
    <path class="pocket-swoosh pocket-swoosh--green" d="M0 608 H250 Q190 612 150 690 Q110 616 0 618 Z" fill="var(--brand-green)"/>
    <path class="pocket-swoosh pocket-swoosh--navy" d="M215 608 H365 Q320 620 290 684 Q265 620 215 608 Z" fill="var(--brand-navy)"/>

    <!-- cover pocket -->
    <path class="pocket pocket--cover" d="M456 640 L482 608 H917 V816 H456 Z" fill="var(--brand-blue)"/>
    <path class="pocket-swoosh pocket-swoosh--green" d="M482 608 H720 Q640 612 600 690 Q560 616 482 612 Z" fill="var(--brand-green)"/>
    <path class="pocket-swoosh pocket-swoosh--navy" d="M680 608 H850 Q800 620 770 680 Q740 620 680 608 Z" fill="var(--brand-navy)"/>
  </svg>

  <p class="wordmark wordmark--cover"><span class="wordmark-dot"></span>Larkvale Home Health Care</p>
  <p class="wordmark wordmark--back"><span class="wordmark-dot"></span>Larkvale Home Health Care</p>
  <p class="contact-line">4210 Harbor Lane, Suite 3, Brookfield Heights, ON 00000 Phone: 000-555-0142 Fax: 000-555-0143</p>
</div>
</body>
</html>
```